Gym Poster to advertise for our chiropractic business

We are needing a poster for a gym. They are a weight training gym, Copper Ridge Gym. The poster will be 4 ft by 8 ft. This poster will be used for advertising purposes.
Target Market(s)
Athletes, 25 to 45,Men and Women,
Industry/Entity Type
Advertising
Font styles to use
Serif
Sans Serif

```html
<!DOCTYPE html>
<html lang="en">
<head>
<meta charset="utf-8">
<title>Keel Line Chiropractic LLC – Complete Spinal Health</title>
<link rel="stylesheet" href="https://fonts.googleapis.com/css2?family=Cabin:wght@600;700&display=swap">
<style>
  :root {
    --navy: #0f2357;
    --navy-deep: #0a1f55;
    --sky-light: #f4f9fe;
    --sky: #cfe6f8;
    --sky-strong: #8fd0f2;
    --steel: #a9b4be;
    --arrow-warm: #f7c9a4;
    --arrow-pink: #f9c8c8;
    --page: #ffffff;
  }
  * { margin: 0; padding: 0; box-sizing: border-box; }
  html, body { width: 1200px; height: 900px; overflow: hidden; background: var(--page); }
  body { font-family: "Cabin", "Trebuchet MS", sans-serif; color: var(--navy); }

  .poster {
    position: absolute; left: 0; top: 133px; width: 1200px; height: 600px; overflow: hidden;
    background:
      linear-gradient(115deg, rgba(255,255,255,0.85) 0%, rgba(255,255,255,0) 55%),
      linear-gradient(160deg, var(--sky) 0%, var(--sky-light) 40%, var(--sky-light) 60%, var(--sky) 100%);
  }
  .poster__streaks {
    position: absolute; inset: 0;
    background:
      repeating-linear-gradient(-22deg, rgba(255,255,255,0) 0 14px, rgba(255,255,255,0.55) 14px 16px, rgba(255,255,255,0) 16px 31px),
      repeating-linear-gradient(22deg, rgba(160,200,230,0) 0 22px, rgba(160,200,230,0.18) 22px 24px, rgba(160,200,230,0) 24px 47px);
  }
  .poster__texture {
    position: absolute; inset: 0;
    background: linear-gradient(200deg, rgba(143,208,242,0) 55%, rgba(143,208,242,0.55) 80%, rgba(143,208,242,0.2) 100%);
  }

  .brand { position: absolute; left: 100px; top: 40px; display: flex; align-items: center; gap: 34px; }
  .brand__mark { width: 104px; height: 104px; border-radius: 50%; background: var(--navy); }
  .brand__name { font-size: 33px; font-weight: 600; line-height: 1.2; color: var(--navy); }

  .headline {
    position: absolute; left: 20px; top: 281px; width: 530px;
    text-align: center; font-size: 41px; font-weight: 700; line-height: 65px; white-space: nowrap;
  }

  .progress { position: absolute; left: 0; top: 0; }
  .step { position: absolute; font-size: 31px; font-weight: 700; white-space: nowrap; line-height: 1; }
  .step--pain { left: 762px; top: 140px; }
  .step--correction { left: 747px; top: 270px; }
  .step--maintenance { left: 673px; top: 373px; }
  .step--health { left: 500px; top: 484px; }

  .figures {
    position: absolute; left: 965px; top: 25px; width: 200px; height: 522px;
    border-radius: 50% 50% 40% 40% / 14% 14% 6% 6%;
    background:
      radial-gradient(ellipse 70% 55% at 40% 70%, rgba(169,180,190,0.95) 0%, rgba(169,180,190,0) 70%),
      linear-gradient(180deg, var(--navy-deep) 0%, #1b3366 60%, #2e4574 100%);
    box-shadow: 0 0 24px 8px rgba(244,249,254,0.6) inset;
    opacity: 0.92;
  }

  .tagline {
    position: absolute; left: 0; bottom: 0; width: 1200px; height: 53px;
    background: linear-gradient(90deg, var(--navy-deep) 0%, #9aa9b9 50%, var(--navy-deep) 100%);
    text-align: center; font-size: 40px; font-weight: 700; line-height: 53px; color: var(--navy-deep);
  }
</style>
</head>
<body>
  <section class="poster">
    <div class="poster__streaks"></div>
    <div class="poster__texture"></div>

    <div class="brand">
      <div class="brand__mark"></div>
      <div class="brand__name">Keel Line<br>Chiropractic LLC</div>
    </div>

    <h1 class="headline">We specialize in correcting<br>the source of your PAIN</h1>

    <svg class="progress" width="1200" height="600" viewBox="0 0 1200 600" aria-hidden="true">
      <defs>
        <linearGradient id="arrowFade" x1="0" y1="1" x2="1" y2="0">
          <stop offset="0" stop-color="var(--arrow-warm)" stop-opacity="0.15"/>
          <stop offset="0.6" stop-color="var(--arrow-warm)" stop-opacity="0.5"/>
          <stop offset="1" stop-color="var(--arrow-pink)" stop-opacity="0.75"/>
        </linearGradient>
      </defs>
      <path d="M495 492 Q860 470 870 190" fill="none" stroke="url(#arrowFade)" stroke-width="52"/>
      <polygon points="758,192 875,58 985,192" fill="url(#arrowFade)"/>
    </svg>

    <div class="step step--pain">Pain Reduction</div>
    <div class="step step--correction">Correction</div>
    <div class="step step--maintenance">Maintenance</div>
    <div class="step step--health">Complete spinal Health</div>

    <div class="figures" role="img" aria-label="Silhouettes of an overweight man standing behind a muscular man flexing, showing the path to fitness"></div>

    <div class="tagline">COMPLETE SPINAL HEALTH</div>
  </section>
</body>
</html>
```